Business Card Design

I am a criminologist running a research and consultancy business on my own (PKConsultants)
I specialise in looking at fraud and other white-collar crimes. Also governance issues..
I would like a professional business card that would be appropriate both in the academic and business sector as I straddle both sectors. Normal shape - not square.
I am interested in seeing border Word Cloud type projects - black on white or white on black..
Example key words would be fraud, research, qualitative, interviews, quantitative, white-collar, reports, government, surveys, sample, governance, assurance, crime, offenders, prison etc (I can provide a full list if this is the option I go for). I also like Word Cloud borders as attached.
I am also interested in seeing other style business cards. Preferably one colour, plus black and white.
In particular I like black backgrounds with coloured words etc - colours like lime green are good.
I also like blues - especially teal if a traditional white background is chosen.
I don't have a logo - unless anyone can think of anything that's particularly appropriate.
Graphics can be used but they would be simple and stylish (dots, squares, lines, curves etc)
I would like the design to translate simply for a header for a website or blog.
My current website is www.pelling-hurst.com but is out of date in terms of what I do and design.
I have attached a number of things that have caught my eye and inspired me.
I have asked for a one-sided business card in the first instance - however if someone comes up with a good cloud design that might go on one side, I would consider a two-sided one.
Design can be landscape or portrait.
Kind Regards
Meg
Landscape
Contact Information for Business Card
PKConsultants
Dr Margery Pelling-Hurst, MSc, BSc, **
42 Brindle Wold
Stone, Staffordshire
KX27 4QD
+44(0)1620 482917
+44(0)7531 804152
www.pelling-hurst.com
margery@pelling-hurst.com

```html
<!DOCTYPE html>
<html lang="en">
<head>
<meta charset="utf-8">
<title>PKConsultants – Business Card</title>
<link rel="stylesheet" href="https://fonts.googleapis.com/css2?family=Cinzel:wght@500;600&family=Crimson+Text:wght@400;700&display=swap">
<style>
  :root {
    --page-bg: #efedea;
    --green-light: #3fb64b;
    --green-mid: #1fa04a;
    --green-dark: #127536;
    --text-green: #1d9a44;
    --white: #ffffff;
    --band-white: #fbfbfb;
    --band-grey: #e6e6e6;
    --edge-dark: #2f2f2f;
    --ribbon-teal: #8ccfdc;
    --ribbon-gold: #e9b24e;
    --ribbon-lime: #a8c83a;
  }
  * { margin: 0; padding: 0; box-sizing: border-box; }
  html, body {
    width: 1200px;
    height: 802px;
    overflow: hidden;
    background: var(--page-bg);
  }
  .business-card {
    position: absolute;
    left: 60px;
    top: 93px;
    width: 1080px;
    height: 615px;
    border-radius: 34px;
    overflow: hidden;
    background: linear-gradient(90deg, var(--green-light) 0%, var(--green-mid) 50%, var(--green-dark) 100%);
    box-shadow: 0 6px 18px rgba(0,0,0,0.25);
  }
  .card-artwork {
    position: absolute;
    inset: 0;
    width: 100%;
    height: 100%;
  }
  .holder-name,
  .holder-credentials {
    position: absolute;
    left: 40px;
    color: var(--white);
    font-family: "Cinzel", serif;
    font-weight: 600;
    line-height: 1;
    white-space: nowrap;
  }
  .holder-name { top: 54px; font-size: 32px; letter-spacing: 0.5px; }
  .holder-credentials { top: 101px; font-size: 25px; letter-spacing: 0.5px; }
  .company-name {
    position: absolute;
    left: 43px;
    top: 297px;
    font-family: "Crimson Text", serif;
    font-weight: 700;
    font-size: 60px;
    line-height: 1;
    color: var(--text-green);
    text-transform: uppercase;
    letter-spacing: 1px;
    white-space: nowrap;
  }
  .contact-list {
    position: absolute;
    right: 52px;
    top: 255px;
    list-style: none;
    text-align: right;
    font-family: "Crimson Text", serif;
    font-size: 26px;
    line-height: 36px;
    color: var(--text-green);
  }
  .website {
    position: absolute;
    right: 52px;
    top: 532px;
    font-family: "Crimson Text", serif;
    font-size: 34px;
    line-height: 1;
    color: var(--white);
    white-space: nowrap;
  }
</style>
</head>
<body>
  <div class="business-card">
    <svg class="card-artwork" viewBox="0 0 780 444" preserveAspectRatio="none" aria-hidden="true">
      <defs>
        <linearGradient id="band-fill" x1="0" y1="0" x2="1" y2="0.3">
          <stop offset="0" stop-color="var(--band-grey)"/>
          <stop offset="0.5" stop-color="var(--band-white)"/>
          <stop offset="1" stop-color="var(--band-grey)"/>
        </linearGradient>
        <linearGradient id="ribbon-top" x1="0" y1="0" x2="1" y2="0">
          <stop offset="0" stop-color="var(--ribbon-teal)"/>
          <stop offset="0.3" stop-color="var(--ribbon-gold)"/>
          <stop offset="0.65" stop-color="var(--ribbon-lime)"/>
          <stop offset="1" stop-color="var(--ribbon-teal)"/>
        </linearGradient>
        <linearGradient id="ribbon-bottom" x1="0" y1="0" x2="1" y2="0">
          <stop offset="0" stop-color="var(--ribbon-teal)"/>
          <stop offset="0.35" stop-color="var(--ribbon-gold)"/>
          <stop offset="0.7" stop-color="var(--ribbon-lime)"/>
          <stop offset="1" stop-color="var(--ribbon-teal)"/>
        </linearGradient>
      </defs>

      <!-- top ribbon -->
      <path class="ribbon" d="M0,150 C150,155 300,50 450,52 C600,54 700,95 780,108"
            fill="none" stroke="url(#ribbon-top)" stroke-width="12"/>
      <!-- bottom ribbon -->
      <path class="ribbon" d="M780,310 C600,300 420,340 330,400 C260,435 120,400 0,332"
            fill="none" stroke="url(#ribbon-bottom)" stroke-width="12"/>

      <!-- white wave band -->
      <path class="wave-band"
            d="M0,160 C150,165 300,60 450,62 C600,64 700,105 780,118
               L780,300 C600,290 420,330 330,390 C260,425 120,390 0,322 Z"
            fill="url(#band-fill)"/>

      <!-- dark edges -->
      <path d="M0,160 C150,165 300,60 450,62 C600,64 700,105 780,118"
            fill="none" stroke="var(--edge-dark)" stroke-width="3"/>
      <path d="M780,300 C600,290 420,330 330,390 C260,425 120,390 0,322"
            fill="none" stroke="var(--edge-dark)" stroke-width="4"/>
    </svg>

    <div class="holder-name">Dr Margery Pelling</div>
    <div class="holder-credentials">Hurst, MSc, BSc</div>

    <div class="company-name">PKConsultants</div>

    <ul class="contact-list">
      <li class="contact-phone">+44(0)1620 482917</li>
      <li class="contact-mobile">+44(0)7531 804152</li>
      <li class="contact-email">margery@pelling-hurst.com</li>
    </ul>

    <div class="website">www.pelling-hurst.com</div>
  </div>
</body>
</html>
```